Velvetorchid Hair & Beauty Business Card

Velvetorchid Hair & Beauty is a boutique salon located in the picturesque Lake Taupo NZ. The salon is very luxurious, opulent gold gilded mirrors, chandelier lit, contemporary french decor, sets the mood to create beautiful hair, makeup and all beauty services. Just had a new logo design and now after a new business card.
Logo
14 Korowhai Street
Taupo
Phone (07) 548 6193
www.velvetorchid.co.nz
email hair@velvetorchid.co.nz
Marlena Swithin
Also need a space to put in Stylist name, date, appointment time. thanks;)
Another idea is we could incorporate the wallpaper in the back ground either on the back or front or use an ornate glided frame (around the edge of the card) like on my website where my brides photos flash.
Decided against the wall paper but at least you can see our colour theme for the salon.
Updates

Please check out my updated brief . Thanks :)

Target Market(s)

25-60 years plus, mainly mid age females , wanting the best possible service , high standard of workmanship and money not a problem.

Industry/Entity Type

Boutique

Requirements
Must have
• Gold and silver

```html
<!DOCTYPE html>
<html lang="en">
<head>
<meta charset="utf-8">
<title>Velvetorchid Hair &amp; Beauty – Cards</title>
<link href="https://fonts.googleapis.com/css2?family=Questrial&display=swap" rel="stylesheet">
<style>
  :root{
    --backdrop:#eee8df;
    --card-white:#ffffff;
    --gold:#8a7420;
    --gold-light:#c9b46a;
    --gold-pale:#e3dcc6;
    --silver:#5e5e60;
    --rule:#e6ddc8;
    --frame-dark:#b8944f;
    --frame-mid:#dcbd7e;
    --frame-light:#f0dcaa;
    --frame-bead:#9c7c47;
    --stripe-a:#e9ddd3;
    --stripe-b:#f1e9dc;
    --shadow:rgba(60,40,20,.28);
  }
  *{box-sizing:border-box;margin:0;padding:0}
  html,body{width:1200px;height:1000px;overflow:hidden}
  body{background:var(--backdrop);font-family:"Questrial",sans-serif;position:relative}

  .brand-name{font-weight:400;color:var(--silver);letter-spacing:.5px;line-height:1;text-align:center;white-space:nowrap}
  .brand-tagline{display:flex;align-items:center;justify-content:center;gap:12px;color:var(--gold);letter-spacing:1px}
  .brand-tagline::before,.brand-tagline::after{content:"";flex:1;height:2px;background:var(--gold)}
  .ornament{position:absolute}

  /* Appointment card */
  .appointment-card{position:absolute;left:140px;top:105px;width:417px;height:627px;background:var(--card-white);box-shadow:0 6px 16px var(--shadow)}
  .appointment-card .ornament-top{left:70px;top:25px;width:265px;height:60px;border-radius:30px;background:linear-gradient(90deg,transparent,var(--gold-light) 25%,var(--gold-light) 75%,transparent)}
  .appointment-card .brand-name{position:absolute;left:0;right:0;top:100px;font-size:52px}
  .appointment-card .brand-tagline{position:absolute;left:33px;right:40px;top:152px;font-size:14px}
  .appointment-title{position:absolute;left:0;right:0;top:180px;text-align:center;font-size:24px;color:var(--silver)}
  .field{position:absolute;left:35px;right:65px;font-size:22px;color:var(--gold);display:flex;align-items:flex-end;gap:24px}
  .field span{flex:1;border-bottom:1.5px solid var(--rule);height:20px}
  .field-extra{position:absolute;left:55px;right:65px;border-bottom:1.5px solid var(--rule)}
  .appointment-card .ornament-bottom{left:5px;top:500px;width:405px;height:112px;border-radius:50px;background:radial-gradient(ellipse at center,var(--gold-pale),rgba(227,220,198,.35) 60%,transparent 75%)}

  /* Business card */
  .business-card{position:absolute;left:510px;top:470px;width:622px;height:418px;background:linear-gradient(135deg,var(--frame-light),var(--frame-dark) 45%,var(--frame-mid) 70%,var(--frame-dark));box-shadow:0 6px 16px var(--shadow);padding:22px}
  .frame-beading{width:100%;height:100%;background:var(--frame-bead);padding:9px}
  .card-face{position:relative;width:100%;height:100%;background:linear-gradient(90deg,var(--stripe-a) 0%,var(--stripe-b) 30%,var(--stripe-a) 55%,var(--stripe-b) 80%,var(--stripe-a) 100%)}
  .business-card .ornament-top{left:135px;top:25px;width:290px;height:72px;border-radius:36px;background:linear-gradient(90deg,transparent,var(--gold-light) 25%,var(--gold-light) 75%,transparent)}
  .business-card .brand-name{position:absolute;left:0;right:0;top:118px;font-size:62px}
  .business-card .brand-tagline{position:absolute;left:95px;right:95px;top:185px;font-size:17px}
  .contact{position:absolute;left:22px;top:232px;width:270px;text-align:center;color:var(--silver);font-size:21px;line-height:27px}
  .contact .address{font-size:22px}
  .contact .web{font-size:19px}
  .stylist{position:absolute;left:330px;top:258px;width:215px;text-align:right}
  .stylist-name{font-size:22px;color:var(--silver)}
  .stylist-role{display:flex;align-items:center;gap:6px;color:var(--gold);font-size:15px;margin-top:8px}
  .stylist-role::before{content:"";flex:1;height:1.5px;background:var(--gold)}
</style>
</head>
<body>

<section class="appointment-card" aria-label="Appointment card">
  <div class="ornament ornament-top" role="img" aria-label="Gold scrollwork flourish ornament"></div>
  <h1 class="brand-name">Velvetorchid</h1>
  <div class="brand-tagline">HAIR &amp; BEAUTY</div>
  <h2 class="appointment-title">Appointment</h2>
  <div class="field" style="top:240px">NAME:<span></span></div>
  <div class="field-extra" style="top:300px"></div>
  <div class="field" style="top:335px">DATE:<span></span></div>
  <div class="field-extra" style="top:403px"></div>
  <div class="field" style="top:428px">TIME:<span></span></div>
  <div class="ornament ornament-bottom" role="img" aria-label="Faint gold scrollwork flourish ornament"></div>
</section>

<section class="business-card" aria-label="Business card with gilded frame">
  <div class="frame-beading" role="img" aria-label="Ornate gilded beaded frame border">
    <div class="card-face">
      <div class="ornament ornament-top" role="img" aria-label="Gold scrollwork flourish ornament"></div>
      <h1 class="brand-name">Velvetorchid</h1>
      <div class="brand-tagline">HAIR &amp; BEAUTY</div>
      <address class="contact" style="font-style:normal">
        <div class="address">14 Korowhai Street, Taupo</div>
        <div class="address">(07) 548 6193</div>
        <div class="web">www.velvetorchid.co.nz</div>
        <div class="web">hair@velvetorchid.co.nz</div>
      </address>
      <div class="stylist">
        <div class="stylist-name">Marlena Swithin</div>
        <div class="stylist-role">STYLIST &amp; OWNER</div>
      </div>
    </div>
  </div>
</section>

</body>
</html>
```